Dog treat Package Design

We’re looking for a creative and professional designer to develop eye-catching packaging for our upcoming line of premium dog treats under the Tailor Munch brand.
The design should reflect quality, trust, and natural nutrition, appealing to dog owners who value healthy, high-end pet products.
What We Need
Full packaging design for a resealable stand-up pouch (approx. 130 × 210 + 60 mm)
Front and back layout including space for logo, product name, ingredients, nutrition panel, barcode, and storage instructions
Print-ready files (with dielines, bleeds, and crop marks)
Editable source file (AI / PSD preferred)
3D mock-up or realistic rendering for presentation
Design Direction
Clean, minimal, and modern look with a premium feel
Use natural tones (e.g. earthy browns, creams, muted greens, or soft neutrals)
Should convey trust, wellness, and craftsmanship
Incorporate subtle texture or illustration that hints at natural ingredients or happy, healthy dogs
Must be consistent across potential product variations (e.g. chicken, beef, lamb treats)
Target Audience
Pet owners who value nutrition, quality ingredients, and design aesthetics — typically aged 25–50, with a focus on healthy, Australian-made pet products.
Deliverables
2 initial design concepts
Up to 2 revision rounds
Final deliverables in:
Print-ready PDF (CMYK)
Editable AI/PSD
High-resolution mock-ups
Design style similar to Fennel Paws
Target Market(s)
People with pets - Premium
Look and feel
Each slider illustrates characteristics of the customer's brand and the style your logo design should communicate.

```html
<!DOCTYPE html>
<html lang="en">
<head>
<meta charset="utf-8">
<title>Tailor Munch Chicken Treats – Pouch Front and Back</title>
<link rel="stylesheet" href="https://fonts.googleapis.com/css2?family=Roboto+Slab:wght@400;600;800;900&family=Catamaran:wght@300;400;600;700&display=swap">
<style>
  :root{
    --page:#ffffff;
    --yellow:#f4cf6e;
    --yellow-deep:#eeba3a;
    --cream:#f3f0dd;
    --cream-dark:#e3dfc4;
    --ink:#2a2a2a;
    --ink-soft:#555555;
    --white:#f6f6f4;
    --accent:#5e9aa8;
    --black:#1c1c1c;
    --rule:#8a8674;
  }
  *{box-sizing:border-box;margin:0;padding:0}
  html,body{width:1200px;height:1200px;overflow:hidden;background:var(--page)}
  .canvas{position:relative;width:1200px;height:1200px}
  .pouch{position:absolute;width:456px;height:685px;background:var(--cream);overflow:hidden}
  .pouch--front{left:106px;top:265px}
  .pouch--back{left:642px;top:262px}

  .band{position:absolute;left:0;top:0;width:100%;height:100px;background:linear-gradient(180deg,var(--yellow),#f7d98a)}
  .band__text{position:absolute;top:22px;left:0;width:100%;text-align:center;font-family:"Roboto Slab",serif;font-weight:400;font-size:14.5px;color:#4a4536;white-space:nowrap}
  .band__text b{font-weight:800}
  .band__text--back{top:30px}

  .dog-art{position:absolute;left:30px;top:50px;width:320px;height:315px;border-radius:46% 50% 8% 8%;
    background:radial-gradient(ellipse at 55% 45%,#bdbbb0 0%,#8c8b86 45%,rgba(120,120,116,0.35) 75%,rgba(243,240,221,0) 100%)}

  .claim-badge{position:absolute;left:355px;top:110px;width:72px;text-align:center}
  .claim-badge__label{font-family:"Roboto Slab",serif;font-size:10px;color:var(--ink-soft);letter-spacing:.5px;display:block;margin-bottom:3px}
  .claim-badge svg{display:block;margin:0 auto}

  .title-block{position:absolute;left:22px;top:362px;width:240px;height:242px;background:linear-gradient(180deg,#f6d88a,var(--yellow-deep))}
  .rooster-art{position:absolute;left:120px;top:20px;width:110px;height:210px;border-radius:40% 40% 20% 20%;
    background:radial-gradient(ellipse at 50% 50%,rgba(234,160,40,.75),rgba(234,160,40,0) 75%)}
  .product-name{position:absolute;left:14px;top:50px;font-family:"Roboto Slab",serif;font-weight:900;font-size:33px;line-height:34px;color:var(--black)}
  .product-desc{position:absolute;left:15px;top:120px;font-family:"Catamaran",sans-serif;font-weight:400;font-size:18px;line-height:20px;color:var(--ink);width:230px}

  .brand-block{position:absolute;left:262px;top:362px;width:178px;height:240px;background:linear-gradient(180deg,var(--white),#e4e4e2)}
  .brand{position:absolute;left:0;width:100%;display:flex;align-items:center;justify-content:center;gap:8px}
  .brand__dot{display:block;width:22px;height:22px;border-radius:50%;background:var(--accent);flex:none}
  .brand__name{font-family:"Roboto Slab",serif;font-weight:800;font-size:17px;color:var(--ink);white-space:nowrap}
  .pouch--front .brand{top:82px}

  .callout{position:absolute;left:18px;top:168px;width:140px;height:58px;border-radius:7px;background:var(--black);
    font-family:"Roboto Slab",serif;font-weight:600;font-size:10.5px;line-height:13px;color:var(--yellow);text-align:center;padding-top:9px}

  .strip{position:absolute;left:0;top:602px;width:100%;height:83px;background:linear-gradient(180deg,var(--cream),var(--cream-dark))}
  .stat{position:absolute;top:18px;text-align:center;font-family:"Catamaran",sans-serif;font-weight:400;font-size:14px;line-height:16px;color:var(--ink)}
  .stat b{display:block;font-family:"Roboto Slab",serif;font-weight:800;font-size:14px}
  .stat--reward{left:8px;width:172px}
  .stat--chicken{left:195px;width:140px}
  .stat--weight{left:360px;width:85px;top:26px;font-family:"Roboto Slab",serif;font-weight:800;font-size:19px}
  .divider{position:absolute;top:10px;height:62px;border-left:1px dashed var(--rule)}
  .divider--one{left:183px}
  .divider--two{left:345px}

  .story{position:absolute;left:37px;top:110px;width:384px;font-family:"Catamaran",sans-serif;font-weight:400;font-size:15px;line-height:21px;color:var(--ink-soft)}
  .story__title{font-weight:700;margin-bottom:2px}
  .story b{font-weight:700;color:#3a3a3a}
  .rule{position:absolute;left:40px;width:370px;border-top:1px dashed var(--rule)}
  .rule--top{top:262px}
  .rule--bottom{top:352px}
  .icons{position:absolute;left:40px;top:272px;width:372px;display:flex;justify-content:space-between}
  .icon{width:70px;text-align:center}
  .icon__label{font-family:"Roboto Slab",serif;font-weight:800;font-size:6.5px;color:var(--ink);display:block;margin-bottom:4px;white-space:nowrap}
  .icon svg{display:block;margin:0 auto}

  .info-block{position:absolute;left:25px;top:360px;width:233px;height:245px;background:linear-gradient(180deg,#f6d88a,var(--yellow-deep))}
  .info{position:absolute;left:8px;top:22px;font-family:"Catamaran",sans-serif;font-weight:400;font-size:15px;line-height:16px;color:var(--ink)}
  .info dt{font-weight:700}
  .info dd{margin-bottom:10px}
  .pouch--back .brand-block{left:258px;top:358px;width:182px;height:247px}
  .pouch--back .brand{top:112px}
  .band__text--bottom{top:30px;color:var(--black)}
</style>
</head>
<body>
<main class="canvas">

  <section class="pouch pouch--front" aria-label="Pouch front">
    <div class="band"><p class="band__text">Tailor Munch <b>Chicken</b> Treats • Tailor Munch <b>Chicken</b> Treats</p></div>
    <div class="dog-art" role="img" aria-label="Engraved-style illustration of a happy dog in profile"></div>

    <div class="claim-badge">
      <span class="claim-badge__label">GRAIN FREE</span>
      <svg width="66" height="66" viewBox="0 0 66 66" aria-hidden="true">
        <circle cx="33" cy="33" r="32" fill="#3a3a3a"/>
        <circle cx="33" cy="33" r="22" fill="none" stroke="#f3f0dd" stroke-width="2.5"/>
        <line x1="33" y1="20" x2="33" y2="46" stroke="#f3f0dd" stroke-width="2"/>
        <line x1="18" y1="18" x2="48" y2="48" stroke="#f3f0dd" stroke-width="2.5"/>
      </svg>
    </div>

    <div class="title-block">
      <div class="rooster-art" role="img" aria-label="Faint orange illustration of a rooster"></div>
      <h1 class="product-name">Chicken<br>Treats</h1>
      <p class="product-desc">Biscuits made with<br>Free-range, Pasture-raised<br>Chicken</p>
    </div>

    <div class="brand-block">
      <div class="brand"><span class="brand__dot"></span><p class="brand__name">Tailor Munch</p></div>
      <p class="callout">A wholesome snack,<br>perfect for training or<br>treating Dogs and Pups</p>
    </div>

    <div class="strip">
      <p class="stat stat--reward"><b>100%</b>Reward for being a good Dog</p>
      <span class="divider divider--one"></span>
      <p class="stat stat--chicken"><b>100%</b>Free Range Chicken</p>
      <span class="divider divider--two"></span>
      <p class="stat stat--weight">200g</p>
    </div>
  </section>

  <section class="pouch pouch--back" aria-label="Pouch back">
    <div class="band"><p class="band__text band__text--back">Tailor Munch <b>Chicken</b> Treats • Tailor Munch <b>Chicken</b> Treats</p></div>

    <div class="story">
      <p class="story__title">Crafted with care:</p>
      <p>Our <b>Chicken Treats</b> are made from wholesome ingredients - entirely free from Wheat, Sugar, Preservatives, and Artificial Flavours. Created for Training or Indulgence, they’re a pure expression of quality and care. Inspired by our search for healthier options, we handcraft each batch so your pet enjoys only the very best.</p>
    </div>

    <span class="rule rule--top"></span>
    <div class="icons">
      <div class="icon"><span class="icon__label">GRASS FED</span>
        <svg width="46" height="46" viewBox="0 0 46 46" aria-hidden="true"><circle cx="23" cy="23" r="22" fill="#2e2e2e"/><path d="M13 32 L16 18 M19 32 L21 14 M24 32 L26 16 M29 32 L33 19" stroke="#f3f0dd" stroke-width="2" fill="none"/><line x1="11" y1="32" x2="35" y2="32" stroke="#f3f0dd" stroke-width="2"/></svg></div>
      <div class="icon"><span class="icon__label">HORMONE FREE</span>
        <svg width="46" height="46" viewBox="0 0 46 46" aria-hidden="true"><circle cx="23" cy="23" r="22" fill="#2e2e2e"/><rect x="17" y="19" width="14" height="7" transform="rotate(-35 23 23)" fill="none" stroke="#f3f0dd" stroke-width="2"/><line x1="11" y1="33" x2="18" y2="28" stroke="#f3f0dd" stroke-width="2"/><line x1="29" y1="18" x2="34" y2="14" stroke="#f3f0dd" stroke-width="2"/></svg></div>
      <div class="icon"><span class="icon__label">NO ADDED SALT</span>
        <svg width="46" height="46" viewBox="0 0 46 46" aria-hidden="true"><circle cx="23" cy="23" r="22" fill="#2e2e2e"/><circle cx="23" cy="23" r="15" fill="none" stroke="#f3f0dd" stroke-width="2"/><line x1="12" y1="12" x2="34" y2="34" stroke="#f3f0dd" stroke-width="2"/></svg></div>
      <div class="icon"><span class="icon__label">NO ADDED SPICES</span>
        <svg width="46" height="46" viewBox="0 0 46 46" aria-hidden="true"><circle cx="23" cy="23" r="22" fill="#2e2e2e"/><ellipse cx="20" cy="27" rx="7" ry="6" fill="none" stroke="#f3f0dd" stroke-width="2"/><line x1="25" y1="22" x2="33" y2="13" stroke="#f3f0dd" stroke-width="2.5"/></svg></div>
      <div class="icon"><span class="icon__label">NO ADDED COLOURS</span>
        <svg width="46" height="46" viewBox="0 0 46 46" aria-hidden="true"><circle cx="23" cy="23" r="22" fill="#2e2e2e"/><path d="M16 14 Q11 22 16 26 Q21 22 16 14Z M28 20 Q23 28 28 32 Q33 28 28 20Z" fill="#f3f0dd"/></svg></div>
    </div>
    <span class="rule rule--bottom"></span>

    <div class="info-block">
      <dl class="info">
        <dt>Ingredients:</dt>
        <dd>100% Free-range, Pasture Raised<br>Chicken &amp; Potassium Sorbate</dd>
        <dt>Contact:</dt>
        <dd>Tailor Munch<br>www.tailormunch.com</dd>
      </dl>
    </div>

    <div class="brand-block">
      <div class="brand"><span class="brand__dot"></span><p class="brand__name">Tailor Munch</p></div>
    </div>

    <div class="strip"><p class="band__text band__text--bottom">Tailor Munch <b>Chicken</b> Treats • Tailor Munch <b>Chicken</b> Treats</p></div>
  </section>

</main>
</body>
</html>
```